FestivaLoom Business Cards

Front
Has logo with a design. Website address (www.festivaloom-demo.com)
Has slogan (celebrate every night)
Has phone number (5559183047)
Should be bold and stands out.

Back
Has details about what we offer.

Events
Search upcoming events
Submit events
Party Image Gallery
View and download HQ party images
Sign up as a contributing event photographer and get paid!
Tickets
Sell your event tickets online for free!
Direct pay
No ticket fee

Target Market(s)

These cards will be handed out in clubs and events to patrons.

Industry/Entity Type

Business

Contact Information for Business Card

Should match or mirror our website in some sort of way. Visit the website to get ideas.

Requirements
Must have
• Must be designed for a 3x3 inch card.

```html
<!DOCTYPE html>
<html lang="en">
<head>
<meta charset="utf-8">
<title>FestivaLoom Business Cards</title>
<link href="https://fonts.googleapis.com/css2?family=Varela+Round&display=swap" rel="stylesheet">
<style>
  :root {
    --stage: #3a3a3a;
    --card-dark: #000000;
    --card-light: #f7f7f7;
    --brand-blue: #2fa3d9;
    --brand-pink: #e0318a;
    --text-white: #ffffff;
    --text-grey: #555555;
    --slogan-grey: #9aa3a8;
  }
  * { margin: 0; padding: 0; box-sizing: border-box; }
  html, body { width: 1200px; height: 750px; overflow: hidden; }
  body {
    background: var(--stage);
    font-family: "Varela Round", Arial, sans-serif;
    position: relative;
  }
  .card {
    position: absolute;
    top: 225px;
    width: 300px;
    height: 300px;
    overflow: hidden;
  }
  .card-front { left: 283px; background: var(--card-dark); }
  .card-back { left: 617px; background: var(--card-light); }

  .brand {
    position: absolute;
    left: 0; right: 0;
    display: flex;
    flex-direction: column;
    align-items: center;
  }
  .brand-row { display: flex; align-items: center; gap: 8px; }
  .brand-dot {
    width: 26px; height: 26px; border-radius: 50%;
    background: var(--brand-pink);
  }
  .brand-name {
    font-size: 26px;
    color: var(--brand-blue);
    line-height: 1;
  }
  .brand-slogan {
    margin-top: 4px;
    font-size: 8px;
    letter-spacing: 3.2px;
    color: var(--slogan-grey);
  }
  .card-front .brand { top: 42px; }
  .card-back .brand { top: 124px; }

  .dome { position: absolute; left: 0; top: 0; width: 300px; height: 300px; }

  .contact {
    position: absolute;
    left: 0; right: 0;
    text-align: center;
    color: var(--text-white);
  }
  .contact-phone { top: 216px; font-size: 34px; letter-spacing: 0.5px; }
  .contact-web { top: 255px; font-size: 14px; }

  .offer {
    position: absolute;
    top: 190px; left: 0; right: 0;
    text-align: center;
  }
  .offer-title {
    font-size: 13px;
    font-weight: normal;
    color: var(--brand-blue);
    margin-bottom: 6px;
  }
  .offer-list { list-style: none; }
  .offer-list li {
    font-size: 8.6px;
    line-height: 11.8px;
    color: var(--text-grey);
  }
  .sep {
    display: inline-block;
    width: 4px; height: 4px; border-radius: 50%;
    background: var(--brand-blue);
    margin: 0 2px;
    vertical-align: middle;
  }
</style>
</head>
<body>
  <section class="card card-front">
    <svg class="dome" viewBox="0 0 300 300" aria-hidden="true">
      <path d="M0,300 L0,243 Q8,222 30,218 C40,150 95,113 150,113 C205,113 260,150 270,218 Q292,222 300,243 L300,300 Z"
            fill="var(--brand-blue)" stroke="var(--brand-pink)" stroke-width="2.5"/>
    </svg>
    <div class="brand">
      <div class="brand-row">
        <span class="brand-dot"></span>
        <span class="brand-name">FestivaLoom</span>
      </div>
      <span class="brand-slogan">celebrate every night</span>
    </div>
    <p class="contact contact-phone">5559183047</p>
    <p class="contact contact-web">www.festivaloom-demo.com</p>
  </section>

  <section class="card card-back">
    <div class="brand">
      <div class="brand-row">
        <span class="brand-dot"></span>
        <span class="brand-name">FestivaLoom</span>
      </div>
      <span class="brand-slogan">celebrate every night</span>
    </div>
    <div class="offer">
      <h2 class="offer-title">Events</h2>
      <ul class="offer-list">
        <li>Search upcoming events <span class="sep"></span> Submit events</li>
        <li>Party Image Gallery <span class="sep"></span> View &amp; download HQ party images</li>
        <li>Sign up as a contributing event photographer &amp; get paid!</li>
        <li>Tickets <span class="sep"></span> Sell your event tickets online for free!</li>
        <li>Direct pay <span class="sep"></span> No ticket fee</li>
      </ul>
    </div>
  </section>
</body>
</html>
```